Business Card Design Project

Refresh of logo attached. Require text underneath to be more ledgible, crisper & cleaner.

Overall, staying with same colour scheme need a brighter, crisper, easily readible business card style.

Industry/Entity Type

Business

```html
<!DOCTYPE html>
<html lang="en">
<head>
<meta charset="utf-8">
<title>Harbourline Estate Advisors – Business Card</title>
<link rel="stylesheet" href="https://fonts.googleapis.com/css2?family=Open+Sans:wght@300;400;700&display=swap">
<style>
  :root {
    --page-bg: #ece8e1;
    --card-frame: #2f5866;
    --card-face: #fbfbfa;
    --ink: #2b2b2b;
    --brand-grey: #5a5d61;
    --brand-square: #4a6a86;
    --rule: #6b2e2e;
    --name-band: #4f7590;
    --band-text: #ffffff;
  }
  * { box-sizing: border-box; margin: 0; padding: 0; }
  html, body {
    width: 1200px;
    height: 1000px;
    overflow: hidden;
    background: var(--page-bg);
    font-family: "Open Sans", Arial, sans-serif;
  }
  .canvas {
    width: 1200px;
    height: 1000px;
    display: flex;
    align-items: center;
    justify-content: center;
  }
  .card {
    position: relative;
    width: 860px;
    height: 500px;
    background: var(--card-frame);
    padding: 22px;
    box-shadow: 0 14px 34px rgba(0, 0, 0, 0.18);
  }
  .card-face {
    position: relative;
    width: 100%;
    height: 100%;
    background: var(--card-face);
    overflow: hidden;
  }
  .brand {
    position: absolute;
    left: 46px;
    top: 82px;
    display: flex;
    align-items: center;
    gap: 20px;
  }
  .brand-square {
    width: 68px;
    height: 68px;
    background: var(--brand-square);
  }
  .brand-name {
    font-size: 52px;
    font-weight: 400;
    letter-spacing: 1px;
    color: var(--brand-grey);
    line-height: 1;
    white-space: nowrap;
  }
  .brand-rule {
    position: absolute;
    left: 46px;
    top: 192px;
    width: 510px;
    height: 2px;
    background: var(--rule);
  }
  .brand-tagline {
    position: absolute;
    left: 46px;
    top: 204px;
    font-size: 13px;
    letter-spacing: 3px;
    text-transform: uppercase;
    color: var(--brand-grey);
    white-space: nowrap;
  }
  .contact {
    position: absolute;
    left: 584px;
    top: 72px;
    list-style: none;
    font-size: 19px;
    line-height: 1.5;
    color: var(--ink);
    white-space: nowrap;
  }
  .name-band {
    position: absolute;
    left: 36px;
    top: 292px;
    width: 500px;
    height: 128px;
    background: var(--name-band);
    color: var(--band-text);
    padding: 28px 0 0 52px;
  }
  .person-name {
    font-size: 30px;
    font-weight: 700;
    line-height: 1.15;
    white-space: nowrap;
  }
  .person-title {
    font-size: 23px;
    font-weight: 300;
    line-height: 1.3;
    white-space: nowrap;
  }
</style>
</head>
<body>
  <main class="canvas">
    <article class="card">
      <div class="card-face">
        <div class="brand">
          <span class="brand-square" aria-hidden="true"></span>
          <span class="brand-name">HARBOURLINE</span>
        </div>
        <div class="brand-rule"></div>
        <p class="brand-tagline">Harbourline Estate Advisors</p>

        <ul class="contact">
          <li>T: (416) 555 0148</li>
          <li>M: (647) 555 0193</li>
          <li>daniel@harbourline.ca</li>
          <li>www.harbourline.ca</li>
        </ul>

        <div class="name-band">
          <p class="person-name">Daniel R. Whitfield</p>
          <p class="person-title">Certified Executor Advisor</p>
        </div>
      </div>
    </article>
  </main>
</body>
</html>
```